Homeowners Insurance Provider Website

We are selling homeowners insurance policy / tenants Policy/Flood Insurance in USA in few states and planning expand nationally.

Our target audience are two folds: Customers (Buy policies) and Insurance Agents who wants to work with us to sell our policies to customers. But website should focus 80% on customers and 20% on agents. So, more customer focused user experience. Please note that there is no direct buy option for customers. They always go through insurance agents.

Customer focused, educational that makes buyer journey easy. We don’t want to come off as trying sell something as there is no direct sales involved from website.

Target Market(s)

Homeowners in USA and Insurance agent who sells these insurance.

Industry/Entity Type

Insurance

Number of Pages Required

4 page

Font styles to use
Other font styles liked:
• Open to suggestions

Colors

Designer to choose colors to be used in the design.

Requirements
Must have
• Three most important things: Trustworthy, Authentic, Simple
• Please use colors form logo and grays
• We like: www.brightmeadow.com
• https://www.harborlinden.com/
• We need Agent Look up tool on home page similar to what is shown on example sites.
• Design:
• Home Page - Open to Ideas
• Insurance (Products) Landing Page - Info similar to: https://www.harborlinden.com/insurance/
• Agents Page - https://www.harborlinden.com/agents/
• Claims Page - Information similar to: https://www.harborlinden.com/claims-center/
• Site Navigation:
• Home
• Insurance
• Claims
• Agents
• About Us
• Contact Us
Nice to have
• Elegant, minimal and clean design that reflects trust and authenticity.
Should not have
• Slider or rotating images - prefer flat design. Not over powering design.

```html
<!DOCTYPE html>
<html lang="en">
<head>
<meta charset="UTF-8">
<title>Harthwell Insurance Co.</title>
<link href="https://fonts.googleapis.com/css2?family=Lato:wght@400;700;900&display=swap" rel="stylesheet">
<style>
:root{
  --navy:#1f3b7d;
  --red:#d21f2f;
  --link:#1f6fbf;
  --text:#4a4a4a;
  --muted:#666;
  --gray-bg:#efefef;
  --white:#fff;
  --line:#cfcfcf;
}
*{box-sizing:border-box;margin:0;padding:0}
html,body{width:820px;height:1200px;overflow:hidden;background:var(--white);font-family:'Lato',sans-serif;color:var(--text)}
.page{position:relative;width:820px;height:1200px}

.site-header{position:absolute;top:0;left:0;width:820px;height:64px;display:flex;align-items:center;padding:0 52px}
.brand{display:flex;align-items:center;gap:8px;font-weight:700;color:var(--navy);font-size:15px;letter-spacing:.5px;line-height:1.1}
.brand-mark{width:26px;height:26px;background:var(--navy);border-radius:3px}
.main-nav{margin-left:auto;display:flex;align-items:center;gap:27px;font-size:9px;letter-spacing:.3px}
.main-nav a{color:var(--muted);text-decoration:none}
.main-nav a.active{color:var(--navy);font-weight:700}
.btn-login{background:var(--red);color:var(--white)!important;font-weight:700;padding:9px 15px;border-radius:1px;margin-left:-12px}

.hero{position:absolute;top:64px;left:0;width:820px;height:307px;background:linear-gradient(100deg,#b9a98e 0%,#cfc3ad 35%,#a99d95 60%,#7a6d8f 80%,#5a5f6e 100%)}
.hero-content{position:absolute;left:52px;top:100px;color:var(--white);width:345px}
.hero h1{font-size:26px;font-weight:900;letter-spacing:.3px;margin-bottom:10px;white-space:nowrap;text-shadow:0 1px 3px rgba(0,0,0,.3)}
.hero p{font-size:11.5px;line-height:17px;margin-bottom:12px}
.btn{display:inline-block;background:var(--red);color:var(--white);font-weight:700;text-decoration:none;border-radius:1px}
.hero .btn{font-size:10px;padding:9px 10px}

.products{position:absolute;top:371px;left:0;width:820px;height:355px;text-align:center}
.products h2{font-size:23px;font-weight:700;color:var(--navy);margin-top:25px}
.products .lead{font-size:12px;line-height:20px;color:var(--text);width:672px;margin:14px auto 0}
.product-grid{display:flex;justify-content:space-between;padding:0 54px;margin-top:28px}
.product{width:154px}
.product-icon{width:72px;height:66px;margin:0 auto;background:var(--navy);border-radius:6px}
.product h3{color:var(--red);font-size:14.5px;font-weight:700;margin-top:18px}
.product p{font-size:10px;line-height:18px;color:var(--text);margin-top:4px}

.about-band{position:absolute;top:726px;left:0;width:820px;height:217px;background:var(--gray-bg)}
.about{position:absolute;left:52px;top:32px;width:460px}
.about h2{font-size:22px;color:var(--navy);font-weight:700}
.about p{font-size:9.8px;line-height:20px;margin-top:12px;color:var(--text);width:452px}
.about .btn{font-size:12px;padding:10px 26px;margin-top:19px}
.newsletter{position:absolute;left:544px;top:36px;width:226px;height:146px;background:var(--white);padding:12px 16px}
.newsletter h2{font-size:22px;color:var(--navy);font-weight:700}
.newsletter .field{margin-top:14px;height:31px;border:1px solid #bbb;background:#f6f6f6;font-size:10px;padding:9px 10px;color:var(--muted)}
.newsletter .btn{display:block;text-align:center;margin-top:6px;font-size:12px;padding:9px 0}

.site-footer{position:absolute;top:943px;left:0;width:820px;height:210px;padding:0 52px}
.footer-col{position:absolute;top:32px}
.footer-col h4{font-size:12.5px;color:var(--link);font-weight:700;margin-bottom:8px}
.footer-col li{list-style:none;font-size:10px;line-height:23.3px;color:var(--muted)}
.search{position:absolute;left:604px;top:34px;width:166px;height:29px;border:1px solid var(--line);font-size:10px;color:var(--muted);padding:8px 8px}
.search svg{position:absolute;right:9px;top:9px}
.follow{position:absolute;left:604px;top:95px}
.follow h4{font-size:12.5px;color:var(--link);font-weight:700}
.social{display:flex;gap:12px;margin-top:9px}
.social span{width:14px;height:14px;border-radius:50%;background:#666}
.copyright{position:absolute;top:1153px;left:0;width:820px;height:47px;background:var(--gray-bg);text-align:center;font-size:8.5px;line-height:47px;color:var(--text)}
</style>
</head>
<body>
<div class="page">
  <header class="site-header">
    <div class="brand"><span class="brand-mark"></span><span>HARTHWELL<br>INSURANCE CO.</span></div>
    <nav class="main-nav">
      <a class="active" href="#">HOME</a>
      <a href="#">INSURANCE</a>
      <a href="#">CLAIMS</a>
      <a href="#">AGENTS</a>
      <a href="#">ABOUT US</a>
      <a href="#">CONTACT US</a>
      <a class="btn-login" href="#">LOG IN</a>
    </nav>
  </header>

  <section class="hero" role="img" aria-label="Photo of a smiling couple in front of their two-storey house">
    <div class="hero-content">
      <h1>HOMEOWNERS INSURANCE</h1>
      <p>Vestibulum ante ipsum primis in faucibus orci luctus et ultrices posuere cubilia aliquam nibh a dui iaculis viverra..</p>
      <a class="btn" href="#">Read More</a>
    </div>
  </section>

  <section class="products">
    <h2>Our Products</h2>
    <p class="lead">Vestibulum vel metus sit amet turpis bibendum tincidunt vel sit amet quam. Pellentesque habitant morbi tristique senectus et netus et malesuada fames ac turpis egestas.</p>
    <div class="product-grid">
      <div class="product"><div class="product-icon" role="img" aria-label="Icon of a family beside a house"></div><h3>Homeowners</h3><p>Vestibulum vel metus sit amet turpis bibendum tincidunt vel sit amet quam habitant morbi tristique senectus..</p></div>
      <div class="product"><div class="product-icon" role="img" aria-label="Icon of an apartment building"></div><h3>Renters/Condo</h3><p>Vestibulum vel metus sit amet turpis bibendum tincidunt vel sit amet quam habitant morbi tristique senectus..</p></div>
      <div class="product"><div class="product-icon" role="img" aria-label="Icon of a house with a flame"></div><h3>Dwelling Fire</h3><p>Vestibulum vel metus sit amet turpis bibendum tincidunt vel sit amet quam habitant morbi tristique senectus..</p></div>
      <div class="product"><div class="product-icon" role="img" aria-label="Icon of a person standing on a location marker"></div><h3>Agent Locator Tool</h3><p>Vestibulum vel metus sit amet turpis bibendum tincidunt vel sit amet quam habitant morbi tristique senectus..</p></div>
    </div>
  </section>

  <section class="about-band">
    <div class="about">
      <h2>About Us</h2>
      <p>Vestibulum vel metus sit amet turpis bibendum tincidunt vel sit amet quam. Pellentesque habitant morbi tristique senectus&nbsp; et netus et malesuada fames ac turpis egestas. Sed vel magna vel eros adipiscing adipiscing eu sit amet turpis. Mauris et massa sed lacus tempus pellentesque.</p>
      <a class="btn" href="#">Read More</a>
    </div>
    <div class="newsletter">
      <h2>Newsletter</h2>
      <div class="field">Enter Email Address</div>
      <a class="btn" href="#">Sign Up</a>
    </div>
  </section>

  <footer class="site-footer">
    <div class="footer-col" style="left:53px"><h4>Our Company</h4><ul><li>Home</li><li>Insurance</li><li>Claims</li><li>Agents</li><li>About us</li><li>Contact us</li></ul></div>
    <div class="footer-col" style="left:242px"><h4>Products</h4><ul><li>Homeowners</li><li>Renters/Condo</li><li>Dwelling Fire</li><li>Agent Locator Tool</li></ul></div>
    <div class="footer-col" style="left:430px"><h4>Connect with Us</h4><ul><li>Support</li><li>Careers</li></ul></div>
    <div class="search">Search...
      <svg width="10" height="10" viewBox="0 0 10 10"><circle cx="4" cy="4" r="3" fill="none" stroke="#1f6fbf" stroke-width="1.5"/><line x1="6.2" y1="6.2" x2="9" y2="9" stroke="#1f6fbf" stroke-width="1.6"/></svg>
    </div>
    <div class="follow">
      <h4>Follow us</h4>
      <div class="social"><span aria-label="Social link"></span><span aria-label="Social link"></span><span aria-label="Social link"></span><span aria-label="Social link"></span><span aria-label="Social link"></span></div>
    </div>
  </footer>
  <div class="copyright">Copyright © 2018. Company Name. All Right Reserved</div>
</div>
</body>
</html>
```